Tactical Supply Company needing memorable business card design

Our tactical supply comapny is in need of a new business card design that will set us apart from the amateurs. We sell tactical gear ranging from backpacks and range bags to apparel and other gear. We are looking for a sharp design that incorporates our logo, website, and name. Our colors are white, red, and black, or any combination of the three, preferably red and black.
I have attached our logo with our name underneath but I have also edited that design with the logo incorporated next to the name (attached).

Target Market(s)

Law enforcement, military, tactical

Industry/Entity Type

Business

Contact Information for Business Card

Include www.fernhollowprovisions-demo.com

Colors
000000
ec1f27
ffffff

Requirements
Must have
• Our name, logo, and website. This is intended to be a memorable simple card, no name, address, email, or phone number info is necessary. Designs that do include this additional info will still be considered if they are absolutely spectacular.
Should not have
• A standard template design, I can create that in my own on Cardvellum. I am looking for a new, creative design that is completely unique to my company.

```html
<!DOCTYPE html>
<html lang="en">
<head>
<meta charset="utf-8">
<title>Fern Hollow Provisions – Business Card</title>
<link rel="stylesheet" href="https://fonts.googleapis.com/css2?family=Open+Sans:wght@400;700&display=swap">
<style>
  :root {
    --red: #ec1f27;
    --red-deep: #c4141b;
    --black: #000000;
    --ink: #3a3a3a;
    --muted: #6b6b6b;
    --white: #ffffff;
    --paper: #f7f7f7;
    --stage: #e6e2dc;
  }
  * { box-sizing: border-box; margin: 0; padding: 0; }
  html, body { width: 1200px; height: 1022px; overflow: hidden; }
  body {
    background: var(--stage);
    font-family: "Open Sans", Arial, sans-serif;
    position: relative;
  }
  .card {
    position: absolute;
    left: 197px;
    width: 805px;
    height: 460px;
    background: linear-gradient(160deg, var(--white) 0%, var(--paper) 100%);
    box-shadow: 0 10px 28px rgba(0,0,0,.22);
    overflow: hidden;
  }
  .card--front { top: 36px; }
  .card--back { top: 526px; }
  .card__art { position: absolute; inset: 0; width: 100%; height: 100%; }

  .brand {
    position: absolute;
    display: flex;
    align-items: center;
    gap: 12px;
  }
  .brand__mark {
    width: 18px; height: 18px;
    background: var(--red);
  }
  .brand__name {
    font-weight: 700;
    color: var(--ink);
    letter-spacing: .5px;
    white-space: nowrap;
  }
  .card--front .brand { left: 232px; top: 80px; }
  .card--front .brand__name { font-size: 30px; }
  .card--back .brand { right: 70px; top: 300px; }
  .card--back .brand__name { font-size: 34px; }

  .person { position: absolute; left: 56px; top: 168px; }
  .person__name { font-size: 30px; font-weight: 700; color: var(--ink); line-height: 1.1; }
  .person__role { font-size: 17px; color: var(--red); margin-top: 2px; }

  .contact { position: absolute; left: 56px; top: 240px; list-style: none; }
  .contact__item {
    display: flex; align-items: center; gap: 12px;
    font-size: 16px; color: var(--ink); height: 24px;
    white-space: nowrap;
  }
  .contact__icon {
    width: 17px; height: 17px; background: var(--red);
    display: flex; align-items: center; justify-content: center;
    flex: none;
  }
  .contact__icon svg { width: 11px; height: 11px; }
</style>
</head>
<body>

<section class="card card--front" aria-label="Business card front">
  <svg class="card__art" viewBox="0 0 805 460" aria-hidden="true">
    <circle cx="700" cy="190" r="90" fill="none" stroke="#000" stroke-opacity=".06" stroke-width="30"/>
    <path d="M0 452 C 300 432, 600 372, 805 240 L805 460 L0 460 Z" fill="var(--black)"/>
    <path d="M0 460 C 300 442, 600 384, 805 254 L805 460 Z" fill="var(--red)"/>
    <path d="M320 460 C 500 430, 660 370, 805 290 L805 460 Z" fill="var(--red-deep)" opacity=".35"/>
  </svg>

  <div class="brand">
    <span class="brand__mark"></span>
    <span class="brand__name">Fern Hollow Provisions</span>
  </div>

  <div class="person">
    <p class="person__name">Marek Tolan</p>
    <p class="person__role">Owner</p>
  </div>

  <ul class="contact">
    <li class="contact__item">
      <span class="contact__icon"><svg viewBox="0 0 12 12"><path d="M2 1h3l1 3-1.5 1a6 6 0 0 0 2.5 2.5L8 6l3 1v3a1 1 0 0 1-1 1A9 9 0 0 1 1 2a1 1 0 0 1 1-1z" fill="#fff"/></svg></span>
      00-7310-4482
    </li>
    <li class="contact__item">
      <span class="contact__icon"><svg viewBox="0 0 12 12"><circle cx="6" cy="6" r="4.5" fill="none" stroke="#fff" stroke-width="1.3"/><path d="M1.5 6h9M6 1.5c-2 2.5-2 6.5 0 9M6 1.5c2 2.5 2 6.5 0 9" fill="none" stroke="#fff" stroke-width="1"/></svg></span>
      www.fernhollowprovisions-demo.com
    </li>
    <li class="contact__item">
      <span class="contact__icon"><svg viewBox="0 0 12 12"><rect x="1" y="2.5" width="10" height="7" fill="none" stroke="#fff" stroke-width="1.3"/><path d="M1 2.5l5 4 5-4" fill="none" stroke="#fff" stroke-width="1.3"/></svg></span>
      info@marektolanmail.com
    </li>
    <li class="contact__item">
      <span class="contact__icon"><svg viewBox="0 0 12 12"><path d="M6 1L1 5.5h1.5V11h2.5V8h2v3h2.5V5.5H11z" fill="#fff"/></svg></span>
      2207 Larkspur Avenue, STE 410 Westbridge, OR 97150
    </li>
  </ul>
</section>

<section class="card card--back" aria-label="Business card back">
  <svg class="card__art" viewBox="0 0 805 460" aria-hidden="true">
    <path d="M0 0 L330 0 C 250 90, 140 170, 0 230 Z" fill="var(--black)"/>
    <path d="M0 0 L312 0 C 236 84, 128 160, 0 214 Z" fill="var(--red)"/>
    <circle cx="250" cy="330" r="120" fill="none" stroke="#000" stroke-opacity=".06" stroke-width="34"/>
  </svg>

  <div class="brand">
    <span class="brand__mark"></span>
    <span class="brand__name">Fern Hollow Provisions</span>
  </div>
</section>

</body>
</html>
```